Furniture Design Website Homepage

Brief as attached- Homepage Design

Silver Heron Furniture is a national retail emporium offering high quality, unique Scandinavian furniture, lighting and accessories. We are the market leader in this space and currently have 2 Showrooms – Melbourne & Sydney.

Most recently our business model has evolved from purely importing premium, one off vintage pieces to a more scalable model of representing brands and manufacturers exclusively out of Scandinavia. These partners manufacture today which ensures us of supply & quality.

We have now started to engage scandinavian designers and/or their families to re-introduce designs that have long gone out of production. These items are put back into production under the silver heron brand, and we own the world wide rights to them.

Please ensure you use the brief files attached and the catalogue images when creating the design.

Target Market(s)

Silver Heron Furniture - where beautiful Scandinavian design meets my modern Australian life.

We want our target audience to chose Scandinavian for their homes & for us to be their brand of choice.

The current perception is that we offer beautiful design but that it doesn’t suit everyone’s home / life / style.

Also that we are more expensive than most.

Industry/Entity Type

Retail

Requirements
Must have
• The colour scheme should be red and white as per the catalogue I attached. We like the look and feel of this site www.roomfondly.example

The furniture is more luxurious, so we need to target the upper market with a nice sleek look that makes the furniture look expensive.

```html
<!DOCTYPE html>
<html lang="en">
<head>
<meta charset="utf-8">
<title>Silver Heron Furniture</title>
<link href="https://fonts.googleapis.com/css2?family=PT+Sans:wght@400;700&family=Didact+Gothic&display=swap" rel="stylesheet">
<style>
:root{
  --red:#e2261b;
  --red-dark:#c41a10;
  --beige:#dcd6bd;
  --beige-light:#f3f1e8;
  --wood:#3b2415;
  --wood-light:#5a3a24;
  --ink:#1f1f1f;
  --grey:#555;
  --line:#6a6a6a;
  --white:#fff;
}
*{margin:0;padding:0;box-sizing:border-box}
html,body{width:1200px;height:900px;overflow:hidden}
body{position:relative;font-family:"PT Sans",Arial,sans-serif;color:var(--ink);font-size:12px;
  background:linear-gradient(90deg,var(--wood) 0,var(--wood-light) 25px,var(--wood) 53px,var(--wood) 1150px,var(--wood-light) 1175px,var(--wood) 1200px)}
.abs{position:absolute}
.page{position:absolute;left:53px;top:4px;width:1097px;height:896px;background:var(--white)}
.topstrip{position:absolute;left:53px;top:0;width:1097px;height:4px;background:var(--beige)}
.topstrip::before{content:"";position:absolute;left:0;top:0;width:212px;height:4px;background:var(--red)}
/* header */
.brand{left:58px;top:70px;font-size:37px;font-weight:700;color:#2b2b2b;letter-spacing:-1px}
.brand-mark{left:190px;top:18px;width:48px;height:48px;background:var(--red)}
.tagline{left:298px;top:42px;font-family:"Didact Gothic",sans-serif;font-size:17px;line-height:23px;color:#111}
.cart{left:940px;top:13px;font-size:11.5px;line-height:18px}
.cart .bag{display:inline-block;width:9px;height:10px;background:#f08a1a;margin-left:6px;vertical-align:-1px;border-radius:1px}
.cart a{color:var(--red)}
.checkout{left:1010px;top:68px;width:56px;height:16px;border-radius:8px;background:var(--red);color:#fff;font-size:9.5px;text-align:center;line-height:16px;font-weight:700}
.secure{left:940px;top:96px;font-size:11.5px;font-weight:700}
.secure span{color:#2aa52a}
.lock{left:1089px;top:88px}
.header-rule{left:265px;top:119px;width:885px;height:3px;background:var(--red)}
/* nav */
.nav{left:266px;top:122px;width:884px;height:35px;border-bottom:1px solid #bbb;display:flex;align-items:center;padding-left:3px;font-size:14px}
.nav a{color:var(--ink);text-decoration:none;padding:3px 9px 3px 15px;position:relative}
.nav a::before{content:"";position:absolute;left:4px;top:11px;width:4px;height:4px;background:var(--red)}
.nav a.active{background:var(--beige);border-radius:12px;padding:3px 8px;margin-left:6px}
.nav a.active::before{left:-10px}
.social{top:129px;width:22px;height:22px;border-radius:4px}
.account{left:1004px;top:127px;width:125px;height:27px;border-radius:14px;background:var(--beige);border:1px solid #b9b293;font-size:14px;text-align:center;line-height:25px}
/* sidebar */
.side{left:53px;top:120px;width:212px;height:735px;border-right:1px solid #ccc}
.side-head{position:absolute;left:0;width:212px;background:var(--beige);border-top:2px solid var(--line);border-bottom:1px solid var(--line);font-size:14.5px;padding-left:11px}
.search-input{left:62px;top:164px;width:134px;height:23px;border-radius:12px;border:1px solid #aaa;background:linear-gradient(#e6e6e6,#fff)}
.pill{border-radius:14px;background:linear-gradient(#ee3a2e,var(--red-dark));color:#fff;text-align:center;font-size:13px;border:1px solid #a51208}
.browse{left:78px;top:220px;list-style:none;font-size:11.5px;line-height:18px}
.browse li{padding-left:10px;position:relative}
.browse li::before{content:"";position:absolute;left:0;top:7px;width:3px;height:3px;background:var(--red)}
.filter-label{left:67px;font-size:11.5px}
.select{left:149px;width:104px;height:19px;border:1px solid #999;background:linear-gradient(#e4e4e4,#fff)}
.select::after{content:"";position:absolute;right:0;top:0;width:20px;height:17px;border-left:1px solid #999;background:#f2f2f2}
.select i{position:absolute;right:6px;top:7px;border:4px solid transparent;border-top:5px solid #333;z-index:1}
.keep{left:70px;top:577px;width:185px;font-size:11.5px;line-height:14.5px;padding-left:8px}
.keep::before{content:"";position:absolute;left:0;top:4px;width:3px;height:3px;background:var(--red)}
.red{color:var(--red)}
.privacy{font-size:11.5px;text-decoration:underline}
.quote{left:68px;top:745px;width:185px;font-size:11.5px;line-height:14.5px}
.side-foot{left:53px;top:855px;width:212px;height:45px;background:var(--beige)}
.card{top:874px;width:32px;height:20px;border:1px solid #888}
/* main */
.heading{left:281px;top:162px;font-size:21px;font-weight:700;color:var(--red)}
.intro{left:283px;top:194px;width:836px;font-size:11.5px;line-height:15px}
.hero{left:280px;top:233px;width:535px;height:275px;background:linear-gradient(180deg,#e7e3d6 0,#d9d4c2 185px,#000 185px)}
.hero-photo{left:295px;top:240px;width:350px;height:230px;background:radial-gradient(ellipse at 50% 62%,#c98a4a 0,#b6783c 35%,rgba(180,120,60,0) 65%)}
.hero-title{left:543px;top:277px;font-family:"Didact Gothic",sans-serif;font-size:27px;line-height:28px;color:#222}
.ribbon{left:716px;top:233px}
.tile{left:817px;width:301px;height:87px;background:linear-gradient(90deg,#fbe3e0 0,#f07a70 45%,var(--red) 75%)}
.tile-photo{position:absolute;left:6px;top:8px;width:100px;height:72px;background:linear-gradient(#eee,#cfc8c0);opacity:.8}
.tile-title{position:absolute;right:14px;top:28px;font-family:"Didact Gothic",sans-serif;font-size:28px;color:#fff;line-height:30px}
.tile-link{position:absolute;right:14px;top:60px;font-size:17px;font-weight:700;color:#fff}
.rec-bar{left:280px;top:515px;width:840px;height:33px;background:var(--beige)}
.rec-icon{left:280px;top:515px;width:35px;height:33px;background:var(--red)}
.rec-title{left:326px;top:518px;font-size:20px;font-weight:700}
.prod{top:554px;height:128px;border:1px solid #bbb}
.prod-photo{position:absolute;left:20px;top:10px;right:20px;bottom:10px;border-radius:6px}
.prod-name{top:687px;font-size:11.5px}
.more{top:687px;font-size:11.5px;color:var(--red)}
.price{top:706px;font-size:13px;color:var(--red)}
.add{top:706px;width:70px;height:19px;font-size:11.5px;line-height:17px}
.newsletter{left:280px;top:748px;width:839px;height:102px;background:var(--beige-light);border:1px solid #bdb58f}
.nl-title{left:292px;top:756px;font-size:15px;font-weight:700}
.nl-text{left:292px;top:783px;font-size:12px;line-height:14.5px}
.nl-label{font-size:12px}
.nl-input{height:17px;border:1px solid #aaa;background:#fff}
.footer{left:265px;top:855px;width:885px;height:45px;background:var(--beige);display:flex;justify-content:flex-end;align-items:center;padding-right:31px;font-size:12px;color:#333}
.footer span{margin:0 8px}
</style>
</head>
<body>
<div class="topstrip"></div>
<div class="page"></div>

<!-- header -->
<div class="abs brand-mark"></div>
<div class="abs brand">silver heron</div>
<div class="abs tagline">The Best of Modern and classic<br>Scandinavian Design</div>
<div class="abs cart">Shopping Cart<span class="bag"></span><br>Item : 0<br>Total : $0.00<br><a href="#">View Cart</a></div>
<div class="abs checkout">Check Out</div>
<div class="abs secure"><span>100%</span> SECURE SHOPPING</div>
<svg class="abs lock" width="24" height="26" viewBox="0 0 24 26" aria-hidden="true"><path d="M6 11V7a6 6 0 0 1 12 0v4" fill="none" stroke="#999" stroke-width="3"/><rect x="2" y="11" width="20" height="14" rx="2" fill="#e8c02a"/><path d="M7 18l3 3 7-7" fill="none" stroke="#3a9a2a" stroke-width="2.5"/></svg>
<div class="abs header-rule"></div>

<nav class="abs nav">
  <a class="active" href="#">About Us</a>
  <a href="#">Furniture Restoration</a>
  <a href="#">Media</a>
  <a href="#">FAQ</a>
  <a href="#">Mailing List</a>
  <a href="#">Blog</a>
  <a href="#">Site Search</a>
  <a href="#">Contact Us</a>
</nav>
<div class="abs social" style="left:940px;background:#4fb4e6"></div>
<div class="abs social" style="left:969px;background:#3b5b9a"></div>
<div class="abs account">Account / <b>Log In</b></div>

<!-- sidebar -->
<aside class="abs side">
  <div class="side-head" style="top:2px;height:35px;line-height:33px">Product Search</div>
  <div class="side-head" style="top:74px;height:24px;line-height:22px">Browse Our Range</div>
  <div class="side-head" style="top:194px;height:26px;line-height:24px">View Product By Type</div>
  <div class="side-head" style="top:420px;height:26px;line-height:24px">Keep Up To Date</div>
  <div class="side-head" style="top:580px;height:26px;line-height:24px">Testimonial</div>
</aside>
<div class="abs search-input"><svg style="position:absolute;right:8px;top:5px" width="12" height="12" viewBox="0 0 12 12" aria-hidden="true"><circle cx="4.5" cy="4.5" r="3.3" fill="none" stroke="#d22" stroke-width="1.6"/><path d="M7 7l4 4" stroke="#d22" stroke-width="2"/></svg></div>
<div class="abs pill" style="left:199px;top:164px;width:64px;height:23px;line-height:21px">Search</div>
<ul class="abs browse">
  <li>Furniture</li><li>Furniture Package</li><li>Accessories</li><li>Lighting</li><li>Fabrics</li>
</ul>
<div class="abs filter-label" style="top:355px">Room :</div>
<div class="abs filter-label" style="top:380px">Furniture :</div>
<div class="abs filter-label" style="top:408px">Designers :</div>
<div class="abs filter-label" style="top:435px">Brands :</div>
<div class="abs filter-label" style="top:460px;left:69px">Accessories :</div>
<div class="abs select" style="top:354px"><i></i></div>
<div class="abs select" style="top:380px"><i></i></div>
<div class="abs select" style="top:407px"><i></i></div>
<div class="abs select" style="top:434px"><i></i></div>
<div class="abs select" style="top:460px"><i></i></div>
<div class="abs pill" style="left:102px;top:493px;width:162px;height:27px;line-height:25px">Find Product</div>
<div class="abs keep">Discover <span class="red">Exclusive offers, Products Previews</span> and much more....</div>
<div class="abs pill" style="left:102px;top:640px;width:162px;height:27px;line-height:25px">Join Our Newsletters</div>
<div class="abs privacy" style="left:117px;top:671px">We value your Privocy</div>
<div class="abs quote">“ Lorem ipsum dolor sit amet, consectetur adipiscing elit.<br>olor sit amet, consectetur adipiscing elit. ”<div style="text-align:right;margin-top:10px;padding-right:12px">--- XYZ</div></div>
<div class="abs side-foot"></div>
<div class="abs" style="left:83px;top:858px;font-size:9.5px">All credit Card Accepted</div>
<div class="abs card" style="left:83px;background:#f2f2f2"></div>
<div class="abs card" style="left:118px;background:#e6e6e6"></div>

<!-- main content -->
<h1 class="abs heading">Heading</h1>
<p class="abs intro">Lorem ipsum dolor sit amet, consectetur adipiscing elit. <span class="red">Phasellus eu posuere odio</span>. Phasellus ac augue diam. Aenean at orci quis metus pulvinar semper ut at urna. Ut sagittis tempor nisi, sodales suscipit arcu porta quis.</p>

<div class="abs hero"></div>
<div class="abs hero-photo" role="img" aria-label="Tan leather sofa with matching ottoman under a black pendant lamp"></div>
<div class="abs hero-title">Latest Offer<br><span style="padding-left:78px">Available</span></div>
<svg class="abs ribbon" width="99" height="98" viewBox="0 0 99 98" aria-hidden="true"><polygon points="0,0 38,0 99,60 99,98" fill="#f3c41c"/><text x="62" y="36" transform="rotate(45 62 36)" text-anchor="middle" font-family="PT Sans,sans-serif" font-weight="700" font-size="22" fill="#111">NEW</text></svg>

<div class="abs tile" style="top:235px"><div class="tile-photo" role="img" aria-label="Black leather armchair"></div><div class="tile-title">Furniture</div><div class="tile-link">View Collection »</div></div>
<div class="abs tile" style="top:328px"><div class="tile-photo" role="img" aria-label="Walnut sideboard"></div><div class="tile-title">Accessories</div><div class="tile-link">View Collection »</div></div>
<div class="abs tile" style="top:420px"><div class="tile-photo" role="img" aria-label="Chrome desk lamp"></div><div class="tile-title">Lighting</div><div class="tile-link">View Collection »</div></div>

<div class="abs rec-bar"></div>
<div class="abs rec-icon"></div>
<h2 class="abs rec-title">Recommends</h2>

<div class="abs prod" style="left:281px;width:184px"><div class="prod-photo" role="img" aria-label="Wooden chair with green seat" style="background:linear-gradient(#c9d88a,#d8b98a)"></div></div>
<div class="abs prod" style="left:496px;width:182px"><div class="prod-photo" role="img" aria-label="Two white pendant lamps" style="background:linear-gradient(#f4f4f4,#d8d8d8)"></div></div>
<div class="abs prod" style="left:710px;width:182px"><div class="prod-photo" role="img" aria-label="Green rocking lounge chair" style="background:linear-gradient(#a4d36a,#dcdcdc)"></div></div>
<div class="abs prod" style="left:924px;width:180px"><div class="prod-photo" role="img" aria-label="Oak console table with drawers" style="background:linear-gradient(#e2c9a4,#c9a77c)"></div></div>
<svg class="abs" style="left:390px;top:555px" width="75" height="72" viewBox="0 0 75 72" aria-hidden="true"><polygon points="0,0 22,0 75,52 75,72" fill="#e7e0cc"/><text x="44" y="30" transform="rotate(45 44 30)" text-anchor="middle" font-family="PT Sans,sans-serif" font-size="12" fill="#e2261b">new product</text></svg>
<svg class="abs" style="left:817px;top:555px" width="75" height="72" viewBox="0 0 75 72" aria-hidden="true"><polygon points="0,0 22,0 75,52 75,72" fill="#e7e0cc"/><text x="44" y="30" transform="rotate(45 44 30)" text-anchor="middle" font-family="PT Sans,sans-serif" font-size="12" fill="#e2261b">new product</text></svg>

<div class="abs prod-name" style="left:281px">Product Name</div><div class="abs more" style="left:397px">More Detail</div>
<div class="abs price" style="left:281px">$2,999</div><div class="abs pill add" style="left:391px">Add to Cart</div>
<div class="abs prod-name" style="left:495px">Product Name</div><div class="abs more" style="left:611px">More Detail</div>
<div class="abs price" style="left:495px">$2,999</div><div class="abs pill add" style="left:605px">Add to Cart</div>
<div class="abs prod-name" style="left:709px">Product Name</div><div class="abs more" style="left:825px">More Detail</div>
<div class="abs price" style="left:709px">$2,999</div><div class="abs pill add" style="left:819px">Add to Cart</div>
<div class="abs prod-name" style="left:924px">Product Name</div><div class="abs more" style="left:1036px">More Detail</div>
<div class="abs price" style="left:924px">$2,999</div><div class="abs pill add" style="left:1030px">Add to Cart</div>

<section class="abs newsletter"></section>
<div class="abs nl-title">Join Our <span class="red">Newsletter</span></div>
<div class="abs nl-text">Discover Exclusive offer,<br><span class="red">Product, Prviews, Information<br>on sales</span> and much more.</div>
<div class="abs nl-label" style="left:475px;top:785px">Name :</div>
<div class="abs nl-label" style="left:475px;top:811px">State :</div>
<div class="abs nl-label" style="left:695px;top:785px">E-Mail :</div>
<div class="abs nl-label" style="left:695px;top:811px">Postal Code :</div>
<div class="abs nl-input" style="left:526px;top:786px;width:119px"></div>
<div class="abs select" style="left:526px;top:811px;width:89px;height:17px"><i style="top:6px"></i></div>
<div class="abs nl-input" style="left:781px;top:786px;width:119px"></div>
<div class="abs nl-input" style="left:781px;top:810px;width:119px"></div>
<div class="abs pill" style="left:941px;top:785px;width:162px;height:27px;line-height:25px;font-size:12px">Join Our Newsletter</div>
<div class="abs privacy" style="left:975px;top:815px">We value your privecy</div>

<footer class="abs footer">About Us<span>:</span>Furniture Restoration<span>:</span>Media<span>:</span>FAQ<span>:</span>Mailing List<span>:</span>Blog<span>:</span>Site Search<span>:</span>Contact Us</footer>
</body>
</html>
```